Australia rare honey label

Australia honey brand: Tolvane honey (dunster rare honey)
Honey type: Red Gum, Orange bloosom, Black honey, Quince etc
Require obvious color or symble to distingwish above different type or taste

Target Market(s)

preminum customers

Font styles to use
Decorative
Script

Requirements
Nice to have
• unique idea which is not similar to market other honey brands.
There is a label sample reference for some information if want to know what infor need to be filled into labels

```html
<!DOCTYPE html>
<html lang="en">
<head>
<meta charset="utf-8">
<title>Tolvane Honey Labels</title>
<link href="https://fonts.googleapis.com/css2?family=Open+Sans:wght@400;600;700&family=Roboto+Condensed:wght@400;500&display=swap" rel="stylesheet">
<style>
  :root {
    --page: #ffffff;
    --panel: #0b0906;
    --comb: #1c1610;
    --comb-red: #5a2d1e;
    --comb-amber: #6a4a2c;
    --ink: #111111;
    --white: #ffffff;
    --gold: #e8a033;
    --red-gum: #e8804f;
    --orange-blossom: #ef8c25;
  }
  * { margin: 0; padding: 0; box-sizing: border-box; }
  html, body { width: 1200px; height: 600px; overflow: hidden; background: var(--page); }
  body { position: relative; font-family: "Open Sans", sans-serif; color: var(--ink); }

  .label { position: absolute; top: 0; width: 560px; height: 600px; }
  .label--red-gum { left: 0; }
  .label--orange-blossom { left: 560px; }

  .brand { position: absolute; left: 58px; top: 56px; display: flex; align-items: center; gap: 12px; }
  .brand__mark { width: 22px; height: 22px; border-radius: 50%; background: var(--ink); }
  .brand__name { font-size: 44px; line-height: 60px; font-weight: 400; color: var(--ink); }

  .intro { position: absolute; left: 320px; top: 59px; width: 218px; font-size: 9.5px; line-height: 12.5px; text-align: center; }
  .label--orange-blossom .intro { left: 332px; top: 51px; width: 216px; }

  .panel { position: absolute; left: 30px; top: 138px; width: 532px; height: 422px;
    background:
      radial-gradient(circle at 154px 28px, var(--comb-red) 0, transparent 36px),
      radial-gradient(circle at 370px 20px, var(--comb-red) 0, transparent 34px),
      radial-gradient(circle at 92px 270px, var(--comb-red) 0, transparent 36px),
      linear-gradient(180deg, var(--comb) 0%, var(--panel) 100%); }
  .label--orange-blossom .panel {
    background:
      radial-gradient(circle at 154px 28px, var(--comb-amber) 0, transparent 36px),
      radial-gradient(circle at 382px 28px, var(--comb-amber) 0, transparent 34px),
      radial-gradient(circle at 92px 268px, var(--comb-amber) 0, transparent 36px),
      linear-gradient(180deg, var(--comb) 0%, var(--panel) 100%); }

  .ingredients { position: absolute; left: 318px; top: 156px; font-size: 9.5px; color: var(--white); }

  .nutrition { position: absolute; left: 325px; top: 230px; width: 200px; background: var(--white);
    border: 1px solid var(--ink); font-family: "Roboto Condensed", sans-serif; font-size: 9px; line-height: 12.2px; }
  .nutrition__title { text-align: center; font-size: 11.5px; line-height: 16px; border-bottom: 1px solid var(--ink); }
  .nutrition__serves { display: flex; justify-content: space-around; border-bottom: 1px solid var(--ink); line-height: 13px; }
  .nutrition table { width: 100%; border-collapse: collapse; }
  .nutrition th { font-weight: 400; text-align: center; line-height: 14px; border-bottom: 1px solid var(--ink); border-left: 1px solid var(--ink); }
  .nutrition th:first-child { border-left: none; width: 72px; }
  .nutrition td { padding: 0 3px; }
  .nutrition td + td { border-left: 1px solid var(--ink); padding-left: 12px; }
  .nutrition tbody tr:first-child td { padding-top: 5px; }
  .nutrition tbody tr:last-child td { padding-bottom: 1px; }
  .nutrition__note { text-align: center; border-top: 1px solid var(--ink); line-height: 14px; }

  .address { position: absolute; left: 314px; top: 416px; width: 222px; text-align: center;
    font-size: 12px; line-height: 16px; color: var(--gold); }

  .variety { position: absolute; left: 30px; top: 425px; width: 286px; height: 45px; border-radius: 0 22px 22px 0;
    padding-left: 70px; display: flex; align-items: center; font-size: 23px; font-weight: 700; color: var(--white); }
  .label--red-gum .variety { background: var(--red-gum); }
  .label--orange-blossom .variety { background: var(--orange-blossom); top: 427px; padding-left: 28px; }

  .weight { position: absolute; left: 135px; top: 500px; font-size: 26px; color: var(--white); }
</style>
</head>
<body>

<section class="label label--red-gum">
  <div class="brand"><span class="brand__mark"></span><span class="brand__name">Tolvane</span></div>
  <p class="intro">Honey is a premium, natural product sourced from pure. It's full of flavour and the natural properties of honey make it an enjoyable and healthy choice for daily dietary intake.</p>
  <div class="panel" role="img" aria-label="Dark honeycomb pattern with red-brown cells"></div>
  <p class="ingredients">INGREDIENTS: 100% Pure Australian Honey.</p>
  <div class="nutrition">
    <div class="nutrition__title">NUTRITIONAL INFORMATION</div>
    <div class="nutrition__serves"><span>Serves per pack: 18</span><span>Serve Size: 20g</span></div>
    <table>
      <thead><tr><th></th><th>per serving</th><th>per 100g</th></tr></thead>
      <tbody>
        <tr><td>Energy</td><td>280kJ</td><td>1400kJ</td></tr>
        <tr><td>Protein</td><td>0.06g</td><td>0.3g</td></tr>
        <tr><td>Fat, total</td><td>0.0g</td><td>0.0g</td></tr>
        <tr><td>&nbsp;-saturated</td><td>0.0g</td><td>0.0g</td></tr>
        <tr><td>Carbohydrates</td><td>16.4g</td><td>82.1g</td></tr>
        <tr><td>&nbsp;-sugars*</td><td>16.4g</td><td>82.1g</td></tr>
        <tr><td>Sodium</td><td>2.8mg</td><td>14mg</td></tr>
      </tbody>
    </table>
    <div class="nutrition__note">*Sugars naturally occuring in honey</div>
  </div>
  <p class="address">Tolvane, 123 ABC road, XYZ, BA 4567<br>Australia</p>
  <div class="variety">RED GUM</div>
  <p class="weight">400g</p>
</section>

<section class="label label--orange-blossom">
  <div class="brand"><span class="brand__mark"></span><span class="brand__name">Tolvane</span></div>
  <p class="intro">Honey is a premium, natural product sourced from pure, untouched native Australian flora. It's full of flavour and the natural properties of honeymake it an enjoyable and healthy choice for daily dietary intake.</p>
  <div class="panel" role="img" aria-label="Dark honeycomb pattern with amber cells"></div>
  <p class="ingredients">INGREDIENTS: 100% Pure Australian Honey.</p>
  <div class="nutrition">
    <div class="nutrition__title">NUTRITIONAL INFORMATION</div>
    <div class="nutrition__serves"><span>Serves per pack: 18</span><span>Serve Size: 20g</span></div>
    <table>
      <thead><tr><th></th><th>per serving</th><th>per 100g</th></tr></thead>
      <tbody>
        <tr><td>Energy</td><td>280kJ</td><td>1400kJ</td></tr>
        <tr><td>Protein</td><td>0.06g</td><td>0.3g</td></tr>
        <tr><td>Fat, total</td><td>0.0g</td><td>0.0g</td></tr>
        <tr><td>&nbsp;-saturated</td><td>0.0g</td><td>0.0g</td></tr>
        <tr><td>Carbohydrates</td><td>16.4g</td><td>82.1g</td></tr>
        <tr><td>&nbsp;-sugars*</td><td>16.4g</td><td>82.1g</td></tr>
        <tr><td>Sodium</td><td>2.8mg</td><td>14mg</td></tr>
      </tbody>
    </table>
    <div class="nutrition__note">*Sugars naturally occuring in honey</div>
  </div>
  <p class="address">Tolvane, 123 ABC road, XYZ, BA 4567<br>Australia</p>
  <div class="variety">ORANGE BLOSSOM</div>
  <p class="weight">400g</p>
</section>

</body>
</html>
```